Window posters

We want a design (Smiley tooth shaped/logo attached) that will be posted on a dental office windows (23"x23") with 11 different wording/colors for each tooth.
All 11 will have the office name on top (Maple lane grins) then:
1- Friendly dental place, Family dentistry.
2- Comprehensive, periodic, exams, cleanings, X-rays
3- Urgent care dentistry, dental emergencies, dental pain.
4- Extractions, immediate Guided implants, 3D scans.
5- Painless one day root canal treatment, conservative dentistry.
6- Cosmetic dentistry, bonding, digital smile makeover.
7- Clear aligners, Kindarc, Clarofit.
8- Same day crowns and bridges.
9- Partial and complete dentures, implants Overdenture.
10- All teeth fixed on Implants.
11- Sleep apnea appliances, sleep dentistry.

```html
<!DOCTYPE html>
<html lang="en">
<head>
<meta charset="utf-8">
<title>Maple Lane Grins – Window Posters</title>
<link rel="stylesheet" href="https://fonts.googleapis.com/css2?family=Montserrat:wght@800&display=swap">
<style>
  :root {
    --ink-blue: #1558a0;
    --mark-teal: #10d2c6;
    --mark-edge: #0a9f96;
    --sky-top: #a9e2f5;
    --sky-mid: #dff6fc;
    --paper: #ffffff;
    --band-start: #1558a0;
    --band-end: #12d2c8;
    --band-text: #ffffff;
  }
  * { margin: 0; padding: 0; box-sizing: border-box; }
  html, body {
    width: 799px;
    height: 1200px;
    overflow: hidden;
    background: var(--paper);
  }
  .sheet {
    position: relative;
    width: 799px;
    height: 1200px;
    font-family: "Montserrat", sans-serif;
  }
  .poster {
    position: absolute;
    width: 391px;
    height: 392px;
  }
  .poster--a { left: 0;     top: 0; }
  .poster--b { left: 408px; top: 0; }
  .poster--c { left: 0;     top: 407px; }
  .poster--d { left: 408px; top: 407px; }
  .poster--e { left: 217px; top: 809px; }

  .poster__art {
    position: absolute;
    left: 0; top: 0;
    width: 391px;
    height: 293px;
    background:
      radial-gradient(ellipse at 50% 75%, var(--paper) 0%, rgba(255,255,255,0) 60%),
      linear-gradient(180deg, var(--sky-top) 0%, var(--sky-mid) 35%, var(--paper) 100%);
  }
  .brand {
    position: absolute;
    left: 0; right: 0; top: 20px;
    text-align: center;
    color: var(--ink-blue);
    font-weight: 800;
    line-height: 1;
  }
  .brand__line1 { display: block; font-size: 24px; letter-spacing: 1.5px; }
  .brand__line2 { display: block; font-size: 50px; letter-spacing: 1px; margin-top: 0; }
  .brand__dot {
    position: absolute;
    left: 50%;
    top: 100px;
    width: 178px;
    height: 178px;
    margin-left: -89px;
    border-radius: 50%;
    background: var(--mark-teal);
    border: 2px solid var(--mark-edge);
  }

  .poster__band {
    position: absolute;
    left: 0; top: 304px;
    width: 391px;
    height: 88px;
    display: flex;
    align-items: center;
    justify-content: center;
    text-align: center;
    background: linear-gradient(90deg, var(--band-start) 0%, var(--band-end) 100%);
    color: var(--band-text);
    font-weight: 800;
    font-size: 24px;
    line-height: 25px;
    text-shadow: 1px 1px 2px rgba(0, 0, 0, 0.35);
  }
  .poster__band--raised { top: 301px; height: 91px; }
  .poster__band--tight { font-size: 21px; }
</style>
</head>
<body>
<main class="sheet">

  <section class="poster poster--a">
    <div class="poster__art" role="img" aria-label="Soft faceted light blue background">
      <div class="brand"><span class="brand__line1">MAPLE LANE</span><span class="brand__line2">GRINS</span></div>
      <div class="brand__dot"></div>
    </div>
    <p class="poster__band">Clear Aligners,<br>Kindarc, Clarofit.</p>
  </section>

  <section class="poster poster--b">
    <div class="poster__art" role="img" aria-label="Soft faceted light blue background">
      <div class="brand"><span class="brand__line1">MAPLE LANE</span><span class="brand__line2">GRINS</span></div>
      <div class="brand__dot"></div>
    </div>
    <p class="poster__band poster__band--raised">Same Day<br>Crowns and Bridges.</p>
  </section>

  <section class="poster poster--c">
    <div class="poster__art" role="img" aria-label="Soft faceted light blue background">
      <div class="brand"><span class="brand__line1">MAPLE LANE</span><span class="brand__line2">GRINS</span></div>
      <div class="brand__dot"></div>
    </div>
    <p class="poster__band poster__band--tight">Partial &amp; Complete Dentures,<br>Implants Overdenture.</p>
  </section>

  <section class="poster poster--d">
    <div class="poster__art" role="img" aria-label="Soft faceted light blue background">
      <div class="brand"><span class="brand__line1">MAPLE LANE</span><span class="brand__line2">GRINS</span></div>
      <div class="brand__dot"></div>
    </div>
    <p class="poster__band poster__band--raised">All Teeth Fixed<br>on Implants.</p>
  </section>

  <section class="poster poster--e">
    <div class="poster__art" role="img" aria-label="Soft faceted light blue background">
      <div class="brand"><span class="brand__line1">MAPLE LANE</span><span class="brand__line2">GRINS</span></div>
      <div class="brand__dot"></div>
    </div>
    <p class="poster__band">Sleep Apnea Appliances,<br>Sleep Dentistry.</p>
  </section>

</main>
</body>
</html>
```